Zorveli Foods Web Page Templates

I need two templates designed for a wholesale food/catering business, one template for the home page and the other for detail pages. The overall template should be a simple, clean and clear design. I have provided the existing logo to which the templates should directly relate.
Zorveli Foods supplies food based upon traditional Ghanian recipes to a number of stores across Canberra. In addition, Zorveli Foods offers catering for public and private functions across the Canberra region.
The colours in the logo represent the national colours of Ghana (yellow, green, red and black) and the website content will also include traditional Ghanian Kente patterns which will add further colour elements to the site. On this basis, the template design needs to be fairly sparse so as not to compete with the colourful content of the website detail pages.
There is no requirement for specific pages to be designed, as these will be handled in the CMS implementation.
The information provided in the Word document is only designed to provide a sense of the intended content of the website, not as a requirement for specific pages to be produced.

Target Market(s)

Retail/Wholesale food

Number of Pages Required

2 page

Font styles to use
Serif

Colors

Designer to choose colors to be used in the design.

Requirements
Must have
• Template must accommodate a responsive design
• The logo provided will form the cornerstone of the design
Nice to have
• There
Should not have
• Please do not solicit for extra work or for alternative logo design.

```html
<!DOCTYPE html>
<html lang="en">
<head>
<meta charset="utf-8">
<title>Zorveli Foods</title>
<link rel="stylesheet" href="https://fonts.googleapis.com/css2?family=Catamaran:wght@400;500;600;700&display=swap">
<style>
:root{
  --green:#1fa878;
  --red:#d80f0a;
  --yellow:#f5b82e;
  --orange:#f3a51b;
  --ink:#2b2b2b;
  --slate:#3e3d4f;
  --night:#232323;
  --muted:#9a9a9a;
  --white:#fff;
}
*{margin:0;padding:0;box-sizing:border-box}
html,body{width:1200px;height:2406px;overflow:hidden;background:var(--white)}
body{position:relative;font-family:"Catamaran",sans-serif;color:var(--ink)}
.abs{position:absolute}
/* top bar */
.topbar{left:0;top:0;width:1200px;height:27px;background:var(--green);color:#fff;font-size:9.5px}
.topbar .contact{left:235px;top:8px}
.topbar .contact span{margin-right:18px}
.topbar .social{right:233px;top:8px;display:flex;gap:8px}
.dot{width:10px;height:10px;border-radius:50%;border:1.5px solid #fff}
/* nav */
.nav{left:0;top:27px;width:1200px;height:52px;background:#fff}
.brand{left:236px;top:10px;font-size:25px;font-weight:600;color:var(--red);letter-spacing:.5px}
.menu{right:234px;top:23px;display:flex;gap:25px;font-size:9.5px;font-weight:500;color:#555;text-transform:uppercase;letter-spacing:.3px}
.menu .on{color:#111;font-weight:600}
/* hero */
.hero{left:0;top:79px;width:1200px;height:455px;overflow:hidden}
.hero-photo{width:100%;height:100%;background:linear-gradient(100deg,#5b4a3c 0%,#3d3a36 28%,#6a5246 50%,#7c3b2e 62%,#a08c7d 80%,#c9bfb5 100%)}
.hero-shade{left:0;top:0;width:100%;height:100%;background:rgba(0,0,0,.28)}
.hero h1{left:0;top:177px;width:1200px;text-align:center;color:#fff;font-size:33px;font-weight:600}
.btn{left:538px;top:246px;width:125px;height:34px;border-radius:17px;background:var(--orange);color:#fff;font-size:11px;font-weight:600;letter-spacing:.5px;text-align:center;line-height:35px}
.arrow{width:33px;height:33px;border-radius:50%;background:#fff;top:189px}
.arrow svg{position:absolute;left:11px;top:10px}
.hero-curve{left:0;top:0}
/* about */
.portrait{left:266px;top:574px;width:285px;height:318px;background:linear-gradient(180deg,#f4f1ee 0%,#c9b3a4 35%,#2a8a92 70%,#1d7078 100%)}
.about{left:565px;top:620px;width:372px;text-align:center}
.about h2{color:var(--red);font-size:18.5px;font-weight:500;letter-spacing:.6px}
.about p{margin-top:19px;font-size:12.2px;line-height:20px;color:#333;letter-spacing:.3px}
.about .taste{margin-top:19px;color:var(--green)}
/* shops */
.shops{left:0;top:892px;width:1200px;height:594px;background:var(--yellow)}
.scallop{left:0;top:0;width:1200px;height:6px;background:radial-gradient(circle at 5px 0,#fff 3.6px,transparent 4.2px) 0 0/10px 6px repeat-x}
.shops h2{left:0;top:53px;width:1200px;text-align:center;color:#fff;font-size:22px;font-weight:600;line-height:28px;letter-spacing:.3px}
.card{width:169px;height:149px;background:linear-gradient(#8a7662,#4a3f35);overflow:hidden}
.card::after{content:"";position:absolute;left:0;bottom:0;width:100%;height:60%;background:linear-gradient(transparent,rgba(0,0,0,.7))}
.card span{position:absolute;left:14px;bottom:12px;z-index:1;color:#fff;font-size:11px;font-weight:700;line-height:13px;text-transform:uppercase}
.note{left:0;top:502px;width:1200px;text-align:center;font-style:italic;font-size:10.5px;line-height:15px;color:#333}
/* dishes */
.band-red{background:var(--red)}
.dishes-title{left:278px;top:1578px;color:#fff;font-size:23px;font-weight:600;line-height:26px}
.dish{overflow:hidden;background:linear-gradient(160deg,#e9e4dc 0%,#b46a3e 45%,#6a3020 100%)}
.dish::after{content:"";position:absolute;left:0;bottom:0;width:100%;height:45%;background:linear-gradient(transparent,rgba(0,0,0,.65))}
.dish span{position:absolute;left:19px;bottom:16px;z-index:1;color:#fff;font-size:13px;font-weight:600;line-height:15px;text-transform:uppercase}
.offer{left:235px;top:1707px;width:295px;height:221px;background:var(--slate);color:#fff}
.offer h3{position:absolute;left:28px;top:76px;font-size:23px;font-weight:600}
.offer p{position:absolute;left:30px;width:240px;font-size:9.8px;line-height:15px}
/* footer */
.footer{left:0;top:1990px;width:1200px;height:416px}
.flogo{left:236px;top:105px;font-size:25px;font-weight:600;color:var(--orange)}
.ftext{left:236px;top:163px;width:200px;font-size:10px;line-height:15px;color:#aaa}
.fsocial{left:236px;top:254px;display:flex;gap:10px}
.fsocial i{display:block;width:22px;height:22px;border-radius:50%;background:#333}
.fhead{top:111px;color:#fff;font-size:12.5px;font-weight:600;letter-spacing:.3px}
.fhead::after{content:"";display:block;width:44px;height:2px;background:var(--orange);margin-top:7px}
.finfo{font-size:10px;line-height:14px;color:#aaa}
.flinks{left:650px;top:162px;font-size:10px;color:#aaa;line-height:22.5px;list-style:none}
.flinks li::before{content:"› ";color:var(--green)}
.nl-text{left:772px;top:163px;width:200px;font-size:8.5px;line-height:18px;color:#ccc}
.nl-field{left:773px;top:223px;width:193px;height:27px;border-radius:14px;background:#fff;font-size:9px;color:#888;line-height:28px;padding-left:27px}
.nl-send{left:941px;top:226px;width:22px;height:22px;border-radius:50%;background:var(--orange)}
.rule{left:236px;top:342px;width:730px;height:1px;background:#3a3a3a}
.copy{left:236px;top:373px;font-size:8.5px;color:#777}
.copy b{color:var(--orange);font-weight:500}
.legal{right:234px;top:373px;font-size:8.5px;color:#777}
</style>
</head>
<body>

<header class="abs topbar">
  <div class="abs contact"><span>Phone : +61 400 555 019</span><span>Email : orders@zorvelimail.com</span></div>
  <div class="abs social"><i class="dot"></i><i class="dot"></i></div>
</header>

<nav class="abs nav">
  <div class="abs brand">Zorveli Foods</div>
  <div class="abs menu"><span class="on">Home</span><span>About us</span><span>Menu</span><span>Gallery</span><span>Locations</span><span>Contact us</span></div>
</nav>

<section class="abs hero">
  <div class="hero-photo" role="img" aria-label="Collage of market stall photos, founder at her stall and plated Ghanaian dishes"></div>
  <div class="abs hero-shade"></div>
  <h1 class="abs">Zorveli Foods commenced in 2004</h1>
  <div class="abs btn">CONTACT US</div>
  <div class="abs arrow" style="left:148px"><svg width="10" height="12" viewBox="0 0 10 12"><path d="M7 1 2 6l5 5" fill="none" stroke="#333" stroke-width="1.6"/></svg></div>
  <div class="abs arrow" style="left:1018px"><svg width="10" height="12" viewBox="0 0 10 12"><path d="M3 1l5 5-5 5" fill="none" stroke="#333" stroke-width="1.6"/></svg></div>
  <svg class="abs hero-curve" width="1200" height="455" viewBox="0 0 1200 455">
    <path d="M0 379 Q600 535 1200 379 L1200 455 L0 455 Z" fill="#fff"/>
    <path d="M0 379 Q600 535 1200 379" fill="none" stroke="#d80f0a" stroke-width="5"/>
  </svg>
</section>

<div class="abs portrait" role="img" aria-label="Portrait photo of the founder in a teal top"></div>
<section class="abs about">
  <h2>Zorveli Foods commenced in 2004</h2>
  <p>Coming from Ghana and with a passion for cooking I realized, through school P&amp;C fundraising, that as well as enjoying my dishes, people wanted to learn more about Ghanaian food. So I started introducing pre-packaged meals at farmers' markets and food festivals to showcase Ghanaian food far and wide. They took off! People relished the exotic flavours. So why don't you give it a go?</p>
  <p class="taste">Have a taste! Enjoy!!</p>
</section>

<section class="abs shops">
  <div class="abs scallop"></div>
  <h2 class="abs">OUR BEAUTIFUL FRESHLY MADE FOOD IS<br>AVAILABLE WEEKLY IN THE FOLLOWING SHOPS:</h2>
  <div class="abs card" style="left:235px;top:146px" role="img" aria-label="Shopfront of farmers outlet"><span>Harvest Lane Curtin</span></div>
  <div class="abs card" style="left:423px;top:146px;background:linear-gradient(#b3241f,#4a3a35)" role="img" aria-label="Supermarket entrance"><span>Ainslie Grocer</span></div>
  <div class="abs card" style="left:610px;top:146px;background:linear-gradient(#c9cdd2,#4f6b3c)" role="img" aria-label="Supermarket sign and trees"><span>Deakin Fresh Mart</span></div>
  <div class="abs card" style="left:797px;top:146px;background:linear-gradient(#7d7f80,#3a3b3c)" role="img" aria-label="Cafe storefront"><span>Ember Goodfoods,<br>Braddon</span></div>
  <div class="abs card" style="left:328px;top:316px;background:linear-gradient(#6d5040,#2f2a28)" role="img" aria-label="Health food shop interior"><span>Green Basket,<br>Mawson</span></div>
  <div class="abs card" style="left:516px;top:316px;background:linear-gradient(#a87c5a,#3b2a22)" role="img" aria-label="Two women in a fruit shop"><span>Orchard Row Fruits,<br>Belconnen</span></div>
  <div class="abs card" style="left:703px;top:316px;background:linear-gradient(#b8c3d2,#7a3f3a)" role="img" aria-label="Supermarket exterior with parked cars"><span>Lyneham Corner Market</span></div>
  <p class="abs note">We also cater for functions, either cocktail or sit-down dining, where we offer<br>special dishes such as jollof rice, garifortor, etc.</p>
</section>

<div class="abs band-red" style="left:0;top:1485px;width:530px;height:222px"></div>
<h2 class="abs dishes-title">OUR CASSEROLE<br>DISHES INCLUDE:</h2>
<div class="abs dish" style="left:530px;top:1485px;width:218px;height:222px" role="img" aria-label="Chicken and spinach casserole with rice"><span>Chicken and spinach<br>casserole</span></div>
<div class="abs dish" style="left:748px;top:1485px;width:219px;height:222px;background:linear-gradient(200deg,#e9e4dc 0%,#9a4a2a 45%,#5a2a1c 100%)" role="img" aria-label="Spicy beef casserole with rice"><span>Spicy beef casserole</span></div>

<div class="abs offer">
  <svg class="abs" style="left:30px;top:28px" width="42" height="32" viewBox="0 0 42 32"><path d="M4 11h8l16-8v26l-16-8H4z M9 21l3 9h5l-3-9" fill="none" stroke="#fff" stroke-width="2" stroke-linejoin="round"/><path d="M33 10l5-3M34 16h6M33 22l5 3" stroke="#fff" stroke-width="2"/></svg>
  <h3>WE ALSO OFFER:</h3>
  <p style="top:125px">Black-eyed beans snacks served with our home made sweet chilli sauce or traditional Ghanaian chilli sauce.</p>
  <p style="top:185px">Coconut sweet.</p>
</div>
<div class="abs dish" style="left:530px;top:1707px;width:437px;height:221px;background:linear-gradient(110deg,#3a4f7a 0%,#8a3a2a 25%,#e8e2d8 55%,#c0683a 80%,#7b2a24 100%)" role="img" aria-label="Black-eyed beans casserole on a plate over kente cloth"><span>Black-eyed beans casserole</span></div>
<div class="abs band-red" style="left:967px;top:1707px;width:233px;height:221px"></div>

<footer class="abs footer">
  <svg class="abs" style="left:0;top:0" width="1200" height="416" viewBox="0 0 1200 416">
    <path d="M0 93 Q600 -67 1200 93 L1200 416 L0 416 Z" fill="#232323"/>
    <path d="M0 93 Q600 -67 1200 93" fill="none" stroke="#1fa878" stroke-width="5"/>
  </svg>
  <div class="abs flogo">Zorveli Foods</div>
  <p class="abs ftext">Coming from Ghana and with a passion for cooking I realized, through school P&amp;C fundraising, that as well as enjoy-ing my dishes, people wanted to learn more about Ghanaian food.</p>
  <div class="abs fsocial"><i></i><i></i></div>

  <div class="abs fhead" style="left:467px">CONTACT INFO</div>
  <svg class="abs" style="left:467px;top:163px" width="11" height="14" viewBox="0 0 11 14"><path d="M5.5 13S1 8 1 5a4.5 4.5 0 0 1 9 0c0 3-4.5 8-4.5 8z" fill="none" stroke="#1fa878" stroke-width="1.2"/><circle cx="5.5" cy="5" r="1.6" fill="none" stroke="#1fa878"/></svg>
  <p class="abs finfo" style="left:490px;top:164px">14 Larkin Crescent<br>Holder</p>
  <svg class="abs" style="left:467px;top:203px" width="12" height="12" viewBox="0 0 12 12"><path d="M2 1l2.5 0 1 3-1.5 1a7 7 0 0 0 3 3l1-1.5 3 1V11a1 1 0 0 1-1 1A10 10 0 0 1 1 2a1 1 0 0 1 1-1z" fill="none" stroke="#1fa878" stroke-width="1"/></svg>
  <p class="abs finfo" style="left:491px;top:203px">Call Us<br>+61 400 555 019</p>
  <svg class="abs" style="left:467px;top:246px" width="13" height="10" viewBox="0 0 13 10"><rect x=".5" y=".5" width="12" height="9" fill="none" stroke="#1fa878"/><path d="M.5 .5l6 5 6-5" fill="none" stroke="#1fa878"/></svg>
  <p class="abs finfo" style="left:491px;top:245px">Email Us<br>orders@zorvelimail.com</p>

  <div class="abs fhead" style="left:645px">QUICK LINKS</div>
  <ul class="abs flinks"><li>Home</li><li>About us</li><li>Menu</li><li>Gallery</li><li>Locations</li><li>Contact us</li></ul>

  <div class="abs fhead" style="left:772px">NEWSLETTER</div>
  <p class="abs nl-text">Subscribe to get updates right in your inbox.<br>We promise to not send you spams.</p>
  <div class="abs nl-field">Enter email here</div>
  <div class="abs nl-send"><svg style="position:absolute;left:5px;top:5px" width="12" height="12" viewBox="0 0 12 12"><path d="M1 6l10-5-4 10-1.5-4z" fill="#fff"/></svg></div>

  <div class="abs rule"></div>
  <p class="abs copy">Copyright © 2019 <b>Zorveli Foods</b>. All Right Reserved.</p>
  <p class="abs legal">Terms &amp; Condition &nbsp;&nbsp;|&nbsp;&nbsp; Privacy Policy</p>
</footer>

</body>
</html>
```